TownDailyo - Business card + Stationery
"Discover fresh corners of your town, daily!" "Today's leading daily deals +"
TownDailyo - Business card + Stationery - Information Technology
Creative Brief
Use specific fonts
Font used is good but open to new ideas
Bright & Fun-filled
Marcus Delwyn
Creator + Director
marcus@towndailyo.example
towndailyo.example
I am looking for a modern catchy design for a new set of business cards. Looking for stationery such as: email template - small logo with web link - Post card - Note pad etc... Looking for a modern design that contains the web link and text to match business card theme. Open to new ideas. Chatterbook and Chirplet logo "TOWNDAILYO" can be used on the cards too. I will make further comments as the various designs come in.
Logo + www. << >>.com on either side of the logo Text at bottom Discover fresh corners of your town, daily

```html
<!DOCTYPE html>
<html lang="en">
<head>
<meta charset="utf-8">
<title>TownDailyo Business Card</title>
<link rel="stylesheet" href="https://fonts.googleapis.com/css2?family=Open+Sans:wght@400;600;700;800&display=swap">
<style>
  :root {
    --bg: #2e2e30;
    --card: #ffffff;
    --blue: #1f7cc4;
    --blue-dark: #15609c;
    --navy: #1c4f8f;
    --pink: #e6338c;
    --green: #8cc63f;
    --orange: #f7941d;
    --yellow: #ffd200;
    --text-grey: #5b6f86;
    --white: #ffffff;
  }
  * { margin: 0; padding: 0; box-sizing: border-box; }
  html, body {
    width: 1200px;
    height: 901px;
    overflow: hidden;
    background: var(--bg);
    font-family: "Open Sans", Arial, sans-serif;
  }
  .stage {
    position: relative;
    width: 1200px;
    height: 901px;
  }
  .card {
    position: absolute;
    left: 250px;
    width: 700px;
    height: 400px;
    background: var(--card);
    overflow: hidden;
    box-shadow: 0 10px 30px rgba(0,0,0,0.45);
  }
  .card-back { top: 30px; }
  .card-front { top: 471px; }

  /* logo block */
  .logo {
    position: absolute;
    display: flex;
    flex-direction: column;
    align-items: center;
  }
  .logo-art {
    width: 190px;
    height: 150px;
    border-radius: 14px;
    background: radial-gradient(circle at 50% 35%, #f6b3d3 0%, #b7dd8a 30%, #ffd67a 55%, #9cc6ea 80%, #e9f2fb 100%);
  }
  .logo-name {
    margin-top: 10px;
    font-weight: 800;
    font-size: 30px;
    color: var(--navy);
    letter-spacing: 0.5px;
  }

  /* back side */
  .card-back .logo { left: 110px; top: 70px; }
  .back-lines {
    position: absolute;
    left: 360px;
    top: 210px;
    color: var(--navy);
  }
  .back-web { font-size: 20px; font-weight: 600; }
  .back-tagline { font-size: 16px; margin-top: 6px; color: var(--text-grey); }

  /* front side */
  .card-front .logo { left: 70px; top: 90px; }
  .stripes {
    position: absolute;
    left: 405px;
    top: 0;
    height: 400px;
    display: flex;
  }
  .stripes span { width: 5px; height: 100%; margin-right: 3px; }
  .stripes .s-pink { background: var(--pink); }
  .stripes .s-green { background: var(--green); }
  .stripes .s-orange { background: var(--orange); }
  .panel {
    position: absolute;
    left: 437px;
    top: 0;
    width: 263px;
    height: 400px;
    background: linear-gradient(180deg, var(--blue) 0%, var(--blue-dark) 100%);
  }
  .person {
    position: absolute;
    right: 26px;
    top: 36px;
    text-align: right;
    color: var(--white);
  }
  .person-name { font-size: 22px; font-weight: 700; }
  .person-role { font-size: 14px; font-weight: 600; margin-top: 2px; }
  .person-web { font-size: 14px; font-weight: 700; margin-top: 2px; }

  .contacts {
    position: absolute;
    right: 26px;
    top: 238px;
    list-style: none;
    color: var(--white);
    font-size: 14px;
  }
  .contacts li {
    display: flex;
    justify-content: flex-end;
    align-items: center;
    gap: 10px;
    height: 25px;
  }
  .contact-icon { width: 16px; height: 16px; flex: none; }
  .social-mark {
    width: 15px;
    height: 15px;
    background: rgba(255,255,255,0.85);
    border-radius: 3px;
    flex: none;
  }
</style>
</head>
<body>
<main class="stage">

  <section class="card card-back" aria-label="Card back">
    <div class="logo">
      <div class="logo-art" role="img" aria-label="Logo illustration: city skyline with colourful curving lines ending in small icons"></div>
      <div class="logo-name">TownDailyo</div>
    </div>
    <div class="back-lines">
      <p class="back-web">www.towndailyo.example</p>
      <p class="back-tagline">Discover fresh corners of your town, daily</p>
    </div>
  </section>

  <section class="card card-front" aria-label="Card front">
    <div class="logo">
      <div class="logo-art" role="img" aria-label="Logo illustration: city skyline with colourful curving lines ending in small icons"></div>
      <div class="logo-name">TownDailyo</div>
    </div>

    <div class="stripes" aria-hidden="true">
      <span class="s-pink"></span>
      <span class="s-green"></span>
      <span class="s-orange"></span>
    </div>

    <div class="panel">
      <div class="person">
        <p class="person-name">Marcus Delwyn</p>
        <p class="person-role">Creator + Director</p>
        <p class="person-web">www.towndailyo.example</p>
      </div>

      <ul class="contacts">
        <li>555-014-2368
          <svg class="contact-icon" viewBox="0 0 16 16" aria-hidden="true">
            <rect x="3" y="1" width="10" height="14" rx="2" fill="none" stroke="#fff" stroke-width="1.5"/>
            <circle cx="8" cy="12.5" r="1" fill="#fff"/>
          </svg>
        </li>
        <li>marcus@towndailyo.example
          <svg class="contact-icon" viewBox="0 0 16 16" aria-hidden="true">
            <rect x="1.5" y="3.5" width="13" height="9" rx="1" fill="none" stroke="#fff" stroke-width="1.5"/>
            <path d="M2 4 L8 9 L14 4" fill="none" stroke="#fff" stroke-width="1.5"/>
          </svg>
        </li>
        <li>TOWNDAILYO <span class="social-mark" aria-hidden="true"></span></li>
        <li>TOWNDAILYO <span class="social-mark" aria-hidden="true"></span></li>
      </ul>
    </div>
  </section>

</main>
</body>
</html>
```